Stationary (letterhead, envelopes, business cards and e-mail signature) for law firm
Law Office of Warren T. Felding
Creative Brief
Professional
Warren T. Felding
Attorney at Law
41 Linden Court, Suite 500 Cedar Vale, California 92731
wfelding@lawwtf-example.com
www.lawwtf-example.com
I would also like my direct dial phone number to appear on the card (in addition to my main number. The Direct number is (714) 555-0187
I would like my logo and maybe my website address to appear on the back. Please be creative.

```html
<!DOCTYPE html>
<html lang="en">
<head>
<meta charset="utf-8">
<title>Law Office of Warren T. Felding — Stationery</title>
<link rel="stylesheet" href="https://fonts.googleapis.com/css2?family=Cinzel:wght@400;600&display=swap">
<style>
  :root {
    --navy: #111a4a;
    --paper: #ffffff;
    --backdrop: #d7d7d9;
    --card-grey: #8a8a8e;
    --silver: #c9cad0;
    --ink-muted: #6d6f7e;
  }
  * { margin: 0; padding: 0; box-sizing: border-box; }
  html, body { width: 1200px; height: 754px; overflow: hidden; }
  body {
    background: var(--backdrop);
    font-family: "Cinzel", serif;
    color: var(--navy);
    position: relative;
  }
  .sheet { position: absolute; background: var(--paper); overflow: hidden; box-shadow: 0 1px 3px rgba(0,0,0,.18); }
  .wave { position: absolute; left: 0; width: 100%; display: block; }

  /* wordmark lockup */
  .lockup { position: absolute; display: flex; align-items: center; gap: 8px; }
  .lockup .mark { font-size: 24px; font-weight: 600; letter-spacing: 1px; color: var(--navy); }
  .lockup .rule { width: 1px; align-self: stretch; background: var(--silver); }
  .lockup .office { font-size: 9px; letter-spacing: 2px; color: var(--ink-muted); line-height: 1.2; }
  .lockup .name { font-size: 15px; letter-spacing: 1px; color: var(--navy); line-height: 1.1; }

  .address { position: absolute; color: #fff; font-size: 9.5px; line-height: 1.55; letter-spacing: .4px; white-space: nowrap; }

  /* letterhead */
  .letterhead { left: 53px; top: 41px; width: 494px; height: 679px; }
  .letterhead .lockup { left: 26px; top: 40px; }
  .letterhead .wave { bottom: 0; height: 110px; }
  .letterhead .address { left: 26px; bottom: 22px; }

  /* business cards */
  .card { position: absolute; border-radius: 9px; overflow: hidden; box-shadow: 0 1px 3px rgba(0,0,0,.2); }
  .card-front { left: 569px; top: 48px; width: 216px; height: 126px; background: var(--paper); }
  .card-front .lockup { left: 10px; top: 10px; gap: 5px; }
  .card-front .lockup .mark { font-size: 14px; }
  .card-front .lockup .office { font-size: 5px; letter-spacing: 1px; }
  .card-front .lockup .name { font-size: 8px; }
  .card-front .holder { position: absolute; left: 70px; top: 40px; text-align: center; }
  .card-front .holder .person { font-size: 8px; color: var(--navy); }
  .card-front .holder .title { font-size: 4.5px; letter-spacing: 1px; color: var(--ink-muted); }
  .card-front .wave { bottom: 0; height: 64px; }
  .card-front .address { left: 10px; top: 80px; font-size: 4.6px; line-height: 1.5; }

  .card-back { display: flex; flex-direction: column; align-items: center; justify-content: center; gap: 8px; }
  .card-back .mark { font-size: 28px; font-weight: 600; letter-spacing: 2px; }
  .card-back .web { font-size: 5.5px; letter-spacing: 1px; }
  .card-white { left: 876px; top: 100px; width: 210px; height: 122px; background: var(--paper); }
  .card-white .mark { color: var(--navy); }
  .card-white .web { color: var(--ink-muted); }
  .card-navy { left: 660px; top: 192px; width: 209px; height: 122px; background: var(--navy); }
  .card-navy .mark, .card-navy .web { color: #fff; }
  .card-grey { left: 895px; top: 244px; width: 211px; height: 122px; background: var(--card-grey); }
  .card-grey .mark, .card-grey .web { color: #fff; }

  /* envelope */
  .envelope { left: 569px; top: 378px; width: 559px; height: 352px; }
  .envelope .flap { top: 0; height: 86px; }
  .envelope .flap-mark { position: absolute; left: 0; right: 0; top: 16px; text-align: center; color: #fff; font-size: 32px; font-weight: 600; letter-spacing: 3px; }
  .envelope .lockup { left: 14px; top: 112px; gap: 6px; }
  .envelope .lockup .mark { font-size: 18px; }
  .envelope .lockup .office { font-size: 6.5px; }
  .envelope .lockup .name { font-size: 11px; }
  .envelope .wave { bottom: 0; height: 100px; }
  .envelope .address { left: 14px; bottom: 24px; font-size: 8.5px; }
</style>
</head>
<body>

<section class="sheet letterhead" aria-label="Letterhead">
  <div class="lockup">
    <span class="mark">WTF</span>
    <span class="rule"></span>
    <div>
      <div class="office">LAW OFFICE OF</div>
      <div class="name">WARREN T. FELDING</div>
    </div>
  </div>
  <svg class="wave" viewBox="0 0 494 110" preserveAspectRatio="none" aria-hidden="true">
    <path d="M0 30 C120 -5 300 60 494 10 L494 110 L0 110 Z" fill="var(--silver)"/>
    <path d="M0 38 C120 5 300 68 494 20 L494 110 L0 110 Z" fill="var(--navy)"/>
  </svg>
  <div class="address">
    41 Linden Court, Suite 500 · Cedar Vale, California 92731<br>
    Phone: (555) 555-0110 · Direct: (714) 555-0187 · Fax: (555) 555-0142<br>
    Email: wfelding@lawwtf-example.com · www.lawwtf-example.com
  </div>
</section>

<section class="card card-front" aria-label="Business card front">
  <div class="lockup">
    <span class="mark">WTF</span>
    <span class="rule"></span>
    <div>
      <div class="office">LAW OFFICE OF</div>
      <div class="name">WARREN T. FELDING</div>
    </div>
  </div>
  <div class="holder">
    <div class="person">WARREN T. FELDING</div>
    <div class="title">ATTORNEY AT LAW</div>
  </div>
  <svg class="wave" viewBox="0 0 216 64" preserveAspectRatio="none" aria-hidden="true">
    <path d="M0 14 C60 26 150 -2 216 8 L216 64 L0 64 Z" fill="var(--navy)"/>
  </svg>
  <div class="address">
    41 Linden Court, Suite 500 · Cedar Vale, California 92731<br>
    Main: (555) 555-0110 · Direct: (714) 555-0187<br>
    wfelding@lawwtf-example.com · www.lawwtf-example.com
  </div>
</section>

<section class="card card-back card-white" aria-label="Business card back, white">
  <span class="mark">WTF</span>
  <span class="web">WWW.LAWWTF-EXAMPLE.COM</span>
</section>

<section class="card card-back card-navy" aria-label="Business card back, navy">
  <span class="mark">WTF</span>
  <span class="web">WWW.LAWWTF-EXAMPLE.COM</span>
</section>

<section class="card card-back card-grey" aria-label="Business card back, grey">
  <span class="mark">WTF</span>
  <span class="web">WWW.LAWWTF-EXAMPLE.COM</span>
</section>

<section class="sheet envelope" aria-label="Envelope">
  <svg class="wave flap" viewBox="0 0 559 86" preserveAspectRatio="none" aria-hidden="true">
    <path d="M0 0 L559 0 L559 66 C420 92 140 92 0 62 Z" fill="var(--navy)"/>
  </svg>
  <div class="flap-mark">WTF</div>
  <div class="lockup">
    <span class="mark">WTF</span>
    <span class="rule"></span>
    <div>
      <div class="office">LAW OFFICE OF</div>
      <div class="name">WARREN T. FELDING</div>
    </div>
  </div>
  <svg class="wave" viewBox="0 0 559 100" preserveAspectRatio="none" aria-hidden="true">
    <path d="M0 30 C150 -5 360 55 559 8 L559 100 L0 100 Z" fill="var(--silver)"/>
    <path d="M0 38 C150 5 360 64 559 18 L559 100 L0 100 Z" fill="var(--navy)"/>
  </svg>
  <div class="address">
    41 Linden Court, Suite 500<br>
    Cedar Vale, California 92731
  </div>
</section>

</body>
</html>
```